Premium Fitness Meal Plan Design for VoltaKor (Brand Like PlumQuarry!)

VoltaKor 6 Week Autumn Forge Meal Plan Design (Branded Handout)

πŸ“„ Overview:
We are looking for a professionally designed, branded meal plan handout for our fitness facility, VoltaKor. This meal plan will be used during our upcoming 6 Week Autumn Forge Quest, where members aim to lose body fat, build lean muscle, and improve their energy through nutrition and strength training.

The design should be highly polished, visually engaging, and reflect our brand quality β€” something on par with what you would see from larger national gym chains (e.g., Plum Quarry, K62, Delmar’s Drillyard). This is not just a text document β€” we want it to feel premium, motivating, and easy to follow, ideally something members are excited to reference and share.

🧾 Format & Layout:
Size: Standard 8.5x11 inch format (single or double-sided)

Final Output: Print-ready PDF + editable source files

Orientation: Portrait

Can be designed as either:

One visually organized front-and-back sheet

Or two clean, digestible pages presented as a mini-handout

🎨 Design Style:
Clean, energetic, and transformation-focused

Use brand colors and fonts that feel bold, fresh, and motivating

Include icons, dividers, or visual cues to separate sections (not just blocks of text)

Sections should feel approachable and empowering, not clinical or restrictive

Include room for the VoltaKor logo (provided) at the top and/or footer

πŸ“˜ Content to Include:
The following content should be visually structured and formatted in clear, engaging blocks. We’ll provide this content in a PDF format

1. Header Title:
"VoltaKor 6 Week Autumn Forge Nutrition Blueprint"

2. Introduction (Small Block):
Short blurb about the challenge goals (lose body fat, gain energy, preserve lean muscle mass)

3. Elimination List (Foods to Avoid):
A visually separated section with a list of foods and drinks that should be eliminated or greatly reduced for fat loss

4. Smart Swaps Table:
A side-by-side "Craving vs Swap" table that shows easy alternatives to popular bad habits (e.g., soda β†’ sparkling water)

5. Build-Your-Own Meal Plan Sections:
Organize these into clear categories:

Proteins

Carbs

Fats

Veggies

Extras / Smart Swaps
Use icons, color codes, or visual grids to organize these food lists

6. Tips Section (Optional Bonuses):
Hydration goal

Suggested number of meals

Protein shake recommendation

Meal timing tip

10-min walk after dinner tip

πŸ“¦ Files Provided:

All written content in organized text format

βœ… Deliverables:
Final design in print-ready PDF

Editable source file (AI, PSD, or InDesign preferred)

πŸ™Œ Inspiration:
Design should feel in line with the type of professional print materials used by high-end fitness studios. Clean lines, engaging fonts, and premium layout. We're not looking for clipart or gimmicky stock photos β€” we want the design to reflect the premium, results-driven experience our gym provides.

```html
<!DOCTYPE html>
<html lang="en">
<head>
<meta charset="utf-8">
<title>VoltaKor 6 Week Autumn Forge Nutrition Blueprint</title>
<link rel="stylesheet" href="https://fonts.googleapis.com/css2?family=Arimo:ital,wght@0,400;0,700;1,400&family=Oswald:wght@300;400&family=Cormorant+Garamond:ital,wght@1,500&family=Tinos:ital,wght@1,400;1,700&display=swap">
<style>
:root{
  --bg:#f7f7f7;
  --paper:#ffffff;
  --cream:#fbebd1;
  --grey:#dcdde2;
  --navy:#0f2b5b;
  --red:#d6372a;
  --blue:#1f3f8f;
  --yellow:#f5d515;
  --green:#2b7d3a;
  --bar:#5e5e60;
  --ink:#1b1b1b;
}
*{box-sizing:border-box;margin:0;padding:0}
html,body{width:1200px;height:846px;overflow:hidden;background:var(--bg)}
body{position:relative;font-family:"Arimo",Arial,sans-serif;color:var(--ink)}
.page{position:absolute;width:447px;height:580px;background:var(--paper)}
.page--front{left:86px;top:128px}
.page--back{left:635px;top:131px}
.panel{position:absolute;left:13px;width:421px;border-radius:14px;overflow:hidden}
.abs{position:absolute}
.heading{font-family:"Oswald",sans-serif;font-weight:300;text-align:center;position:absolute;left:0;right:0;line-height:1}
.script{font-family:"Cormorant Garamond",serif;font-style:italic;font-weight:500;text-align:center;position:absolute;left:0;right:0;line-height:1.25;color:var(--red)}
.chev{position:absolute}

/* header */
.hero{top:13px;height:153px;background:linear-gradient(120deg,#2f56b8 0%,#1d3a8a 55%,#17307a 100%)}
.hero__brand{position:absolute;top:10px;left:0;right:0;text-align:center;font-weight:700;font-size:30px;color:var(--yellow);letter-spacing:-.5px}
.hero__title{position:absolute;top:50px;left:0;right:0;text-align:center;color:#fff;font-weight:700;font-size:25.5px;line-height:26px}
.goal{position:absolute;left:69px;top:107px;width:268px;height:39px;background:#fff;border-radius:5px;text-align:center;font-family:"Tinos",serif;font-style:italic}
.goal__label{font-family:"Arimo",sans-serif;font-style:normal;font-weight:700;color:var(--green);font-size:13px;line-height:15px;padding-top:2px}
.goal__label span{color:#888;font-weight:400;font-size:10px}
.goal__text{font-size:9px;line-height:11px;color:#333}
.goal__text b{font-weight:700}

/* eliminate */
.eliminate{top:176px;height:186px;background:var(--cream)}
.eliminate .heading{top:7px;font-size:17px;color:var(--navy)}
.eliminate .heading small{font-size:13.5px}
.eliminate .script{top:25px;font-size:10.5px}
.no-food{left:18px;top:58px;width:104px;height:104px;border-radius:50%;background:radial-gradient(circle,#e7b46a 0%,#c98a3b 55%,#fff 56%,#fff 64%,var(--red) 65%)}
.elim-list{position:absolute;left:136px;top:40px;list-style:none;font-size:7.3px;line-height:14.4px;white-space:nowrap}
.elim-list li::before{content:"✕";color:var(--red);font-weight:700;margin-right:5px}
.elim-list b{font-weight:700}
.elim-list .tight{font-size:5.9px;letter-spacing:-.1px}

/* swaps */
.swaps{top:372px;height:193px;background:var(--grey)}
.swaps .heading{top:6px;font-size:18.5px;color:var(--red);font-weight:400}
.swaps .script{top:25px;font-size:10.5px;color:var(--navy)}
.swap-table{position:absolute;left:16px;top:54px;border-collapse:collapse;font-size:7.2px}
.swap-table th{font-family:"Oswald",sans-serif;font-weight:300;font-size:13.5px;text-align:left;padding-bottom:3px;color:#222}
.swap-table td{height:11.5px;line-height:11.5px;white-space:nowrap}
.swap-table td:first-child{width:74px}
.swap-table td:last-child::before{content:"✔";color:var(--green);margin-right:4px}
.swap-table .tight{font-size:6.4px}
.good-food{left:321px;top:74px;width:94px;height:94px;border-radius:50%;background:radial-gradient(circle,#f2d27c 0%,#8fb35a 55%,#3ea535 62%,#3ea535 100%)}

/* meal plan */
.meal{top:2px;height:308px;background:var(--cream)}
.meal .heading{top:9px;font-size:18.5px;color:var(--navy);font-weight:400}
.meal .script{top:32px;font-size:10px;padding-left:30px}
.group{position:absolute;border:1.2px solid #6d6d6d;border-radius:5px;background:var(--cream)}
.group__bar{position:relative;background:var(--red);color:#fff;font-weight:700;font-size:10.5px;height:18px;line-height:18px;padding-left:9px;margin:3px 3px 0}
.group__icon{position:absolute;right:6px;top:-4px;width:18px;height:22px;border-radius:50%}
.group__note{font-style:italic;color:var(--green);font-size:7.4px;line-height:12px;padding:4px 6px 0 8px}
.group ul{list-style:none;padding:0 4px 0 3px;font-size:7.4px}
.group li{position:relative;padding-left:7px}
.group li::before{content:"•";position:absolute;left:0;font-weight:700}
.group b{font-weight:700}
.proteins{left:10px;top:65px;width:114px;height:226px}
.proteins li{line-height:9px;margin-bottom:2.2px}
.carbs{left:130px;top:65px;width:113px;height:226px}
.carbs li{line-height:12.3px}
.fats{left:249px;top:65px;width:161px;height:138px}
.fats .group__note{line-height:10.5px;padding-top:4px;padding-bottom:1px}
.fats li{line-height:10.6px}
.veggies{left:249px;top:209px;width:161px;height:82px}
.veggies li{line-height:11px;padding-left:10px}

/* bonus tips */
.bonus{top:314px;height:162px;background:var(--grey)}
.bonus .heading{top:9px;font-size:18.5px;color:var(--red);font-weight:400}
.tip{position:absolute;width:179px}
.tip__bar{height:17px;background:var(--bar);color:#fff;font-weight:700;font-size:8.7px;line-height:17px;padding-left:6px;padding-right:34px;position:relative;white-space:nowrap}
.tip__bar.center{padding-left:30px;padding-right:0;text-align:center}
.tip__icon{position:absolute;width:22px;height:22px;border-radius:50%;background:#fff;border:1.5px solid #222;top:-3px}
.tip__sub{font-size:7.2px;line-height:9px;margin-top:3px;white-space:nowrap}
.tip__sub.wrap{white-space:normal}
.tip__sub.center{text-align:center;padding-left:20px}

/* habits */
.habits{top:482px;height:73px;background:var(--cream)}
.habits .heading{top:3px;font-size:17px;color:var(--navy);font-weight:400}
.pill{position:absolute;height:14px;background:var(--red);color:#fff;font-size:7.3px;line-height:14px;padding-left:31px;border-radius:2px;white-space:nowrap}
.pill__icon{position:absolute;left:4px;top:-2px;width:16px;height:16px;border-radius:3px;background:#2a4b97}
</style>
</head>
<body>

<section class="page page--front">
  <header class="panel hero" role="img" aria-label="Photo of gym members training, tinted blue">
    <svg class="chev" style="left:29px;top:13px" width="36" height="22" viewBox="0 0 36 22" fill="none" stroke="#f5d515" stroke-width="2.5"><path d="M2 2l9 9-9 9M12 2l9 9-9 9M22 2l9 9-9 9"/></svg>
    <div class="hero__brand">VoltaKor</div>
    <h1 class="hero__title">6 WEEK AUTUMN FORGE<br>NUTRITION BLUEPRINT</h1>
    <div class="goal">
      <div class="goal__label"><span>«</span> GOAL <span>»</span></div>
      <div class="goal__text"><b style="color:var(--red)">Drop body fat</b>, <b style="color:#1a7fd0">Maintain lean muscle</b>, and <b style="color:var(--navy)">Boost energy</b><br>without giving up real food or living in the kitchen</div>
    </div>
  </header>

  <section class="panel eliminate">
    <h2 class="heading">FOODS &amp; DRINKS <small>TO ELIMINATE (OR GREATLY REDUCE)</small></h2>
    <p class="script">These are the biggest culprits sabotaging fat loss — highly palatable, calorie-dense, and metabolically disruptive</p>
    <div class="abs no-food" role="img" aria-label="Fast food burgers and fries crossed out by a red prohibition sign"></div>
    <ul class="elim-list">
      <li><b>SUGARY DRINKS</b> (sodas, energy drinks, sweet teas, juice blends)</li>
      <li><b>FANCY COFFEE DRINKS</b> (Frostachinos, sugary creamers, flavor pumps)</li>
      <li><b>FAST FOOD AND FRIED FOODS</b> (even “grilled” items often packed with oils)</li>
      <li><b>PACKAGED SNACKS</b> (chips, cookies, granola bars, trail mix with candy)</li>
      <li><b>BAKED GOODS</b> (donuts, muffins, pastries, bagels with cream cheese)</li>
      <li><b>ALCOHOL</b> (especially beer and sugary mixers)</li>
      <li><b>PROCESSED CARBS</b> (white breads, crackers, pasta)</li>
      <li><b>CHEESE-HEAVY MEALS</b> (pizza, nachos, quesadillas)</li>
      <li><b>HIGH-FAT DELI MEATS</b> (salami, pepperoni, sausage)</li>
      <li class="tight"><b>SAUCES AND CONDIMENTS LOADED WITH SUGAR</b> (ketchup, BBQ sauce, honey mustard)</li>
    </ul>
    <svg class="chev" style="left:374px;top:129px" width="36" height="22" viewBox="0 0 36 22" fill="none" stroke="#e07066" stroke-width="2"><path d="M2 2l9 9-9 9M12 2l9 9-9 9M22 2l9 9-9 9"/></svg>
  </section>

  <section class="panel swaps">
    <svg class="chev" style="left:13px;top:20px" width="36" height="22" viewBox="0 0 36 22" fill="none" stroke="#9a9a9a" stroke-width="2"><path d="M2 2l9 9-9 9M12 2l9 9-9 9M22 2l9 9-9 9"/></svg>
    <h2 class="heading">SMART SWAPS FOR FAT LOSS</h2>
    <p class="script">Instead of cutting everything and feeling deprived, make these easy grocery-store swaps<br>that still satisfy cravings without killing your progress:</p>
    <table class="swap-table">
      <tr><th>CRAVING</th><th>TRY THIS INSTEAD</th></tr>
      <tr><td>SODA</td><td>Sparkling water with lime, Fizzlea, or plain water with fruit infusions</td></tr>
      <tr><td>FANCY COFFEE</td><td>Coffee with unsweetened almond milk + stevia drops or cinnamon</td></tr>
      <tr><td>CHIPS</td><td>Rice cakes, roasted chickpeas, or crunchy cucumber with Chilmara</td></tr>
      <tr><td>ICE CREAM</td><td>Frozen banana blended with protein powder (DIY "nice cream")</td></tr>
      <tr><td>CANDY</td><td>Berries, apples or dark chocolate squares (85%+)</td></tr>
      <tr><td>PASTA</td><td>Zucchini noodles, chickpea pasta, or cauliflower rice</td></tr>
      <tr><td>PIZZA</td><td class="tight">Egg white wraps or low-carb tortillas with turkey pepperoni and light cheese</td></tr>
      <tr><td>ALCOHOL</td><td>Limit to 1x/week if needed</td></tr>
      <tr><td>SANDWICH BREAD</td><td>Elkana bread, low-carb wraps, or lettuce wraps</td></tr>
      <tr><td>HEAVY SAUCES</td><td>Mustard, salsa, hot sauce, coconut aminos, Greek yogurt-based dips</td></tr>
    </table>
    <div class="abs good-food" role="img" aria-label="Healthy plate of eggs, salmon, avocado and vegetables with a green check mark"></div>
  </section>
</section>

<section class="page page--back">
  <section class="panel meal">
    <h2 class="heading">BUILD-YOUR-OWN MEAL PLAN GUIDE</h2>
    <svg class="chev" style="left:15px;top:30px" width="20" height="28" viewBox="0 0 20 28" fill="none" stroke="#e07066" stroke-width="2"><path d="M2 2l8 8 8-8M2 10l8 8 8-8M2 18l8 8 8-8"/></svg>
    <p class="script">Use these fit-friendly food lists to mix &amp; match meals. Your job: choose 1 protein, 1 carb (if desired)<br>and 1 fat or veggie at each meal. Keep it simple, keep it consistent</p>

    <div class="group proteins">
      <div class="group__bar">PROTEINS<span class="group__icon" role="img" aria-label="Egg illustration" style="background:#fff3c4;border:1px solid #333"></span></div>
      <p class="group__note">(Choose 1 per Meal/Snack)</p>
      <ul>
        <li><b>Chicken Breast or Thighs</b> (air fried or grilled)</li>
        <li><b>Lean Gground Beef</b> (90/10 or better)</li>
        <li><b>Ground turkey or turkey breast</b></li>
        <li><b>Center-cut Pork Chops</b></li>
        <li><b>Eggs / Egg whites</b></li>
        <li><b>Tuna</b> (canned in water)</li>
        <li><b>Salmon or White Fish</b></li>
        <li><b>Shrimp</b></li>
        <li><b>Greek Yogurt</b> (plain, low sugar)</li>
        <li><b>Cottage Cheese</b> (low-fat)</li>
        <li><b>Protein Powder</b> (whey or plant-based)</li>
        <li><b>Deli Turkey</b> (low-sodium)</li>
      </ul>
    </div>

    <div class="group carbs">
      <div class="group__bar">CARBS<span class="group__icon" role="img" aria-label="Rice bowl and bread illustration" style="width:28px;border-radius:4px;background:linear-gradient(90deg,#4aa3dc,#e0883a)"></span></div>
      <p class="group__note">(Choose 1–2 Servings per Day, Timed post-workout or Morning)</p>
      <ul>
        <li><b>Jasmine or Basmati Rice</b> (white or brown)</li>
        <li><b>Sweet Potatoes or Yams</b></li>
        <li><b>Rolled Oats or Steel Cut</b></li>
        <li><b>Oats</b></li>
        <li><b>Quinoa</b></li>
        <li><b>Elkana bread</b></li>
        <li><b>Rice Cakes</b></li>
        <li><b>Berries</b> (Blueberries, Raspberries, Strawberries)</li>
        <li><b>Apples / Bananas</b></li>
        <li><b>Chickpeas or Black Beans</b> (in moderation)</li>
      </ul>
    </div>

    <div class="group fats">
      <div class="group__bar">FATS<span class="group__icon" role="img" aria-label="Avocado illustration" style="width:14px;background:#9cc24a"></span></div>
      <p class="group__note">(Add small amounts to Meals, 2–4 Servings/day)</p>
      <ul>
        <li><b>Avocado or Guacamole</b></li>
        <li><b>Olive Oil or Avocado Oil</b> (cooking or drizzle)</li>
        <li><b>Nut Butters</b> (almond, peanut – natural only)</li>
        <li><b>Whole eggs</b></li>
        <li><b>Nuts</b> (almonds, walnuts – portion controlled)</li>
        <li><b>Chia seeds or flax seeds</b></li>
      </ul>
    </div>

    <div class="group veggies">
      <div class="group__bar">VEGGIES<span class="group__icon" role="img" aria-label="Vegetables illustration" style="width:26px;height:28px;top:-6px;background:linear-gradient(135deg,#5aae3c,#e0673a)"></span></div>
      <p class="group__note" style="padding-top:0;padding-left:13px;font-size:8.2px">(unlimited – fill your plate!)</p>
      <ul>
        <li><b>Spinach, Kale, Arugula</b></li>
        <li><b>Zucchini, Asparagus, Bell Peppers</b></li>
        <li><b>Broccoli, Cauliflower, Green Beans</b></li>
        <li><b>Cucumber, Tomatoes, Shredded Carrots</b></li>
      </ul>
    </div>
  </section>

  <section class="panel bonus">
    <svg class="chev" style="left:29px;top:9px" width="36" height="22" viewBox="0 0 36 22" fill="none" stroke="#9a9a9a" stroke-width="2"><path d="M2 2l9 9-9 9M12 2l9 9-9 9M22 2l9 9-9 9"/></svg>
    <h2 class="heading" style="padding-left:5px">BONUS TIPS FOR MAXIMUM RESULTS</h2>

    <div class="tip" style="left:24px;top:40px">
      <div class="tip__bar">Drink 80-120 oz. water daily<span class="tip__icon" role="img" aria-label="Water bottle and glass icon" style="right:10px;border:none;background:#3aa0e0;border-radius:4px;width:14px;height:24px;top:-8px"></span></div>
      <p class="tip__sub" style="font-size:6.9px">Hydration is key for Fat Loss and Muscle Performance</p>
    </div>
    <div class="tip" style="left:219px;top:40px">
      <div class="tip__bar">Two Protein Shakes Allowed<span class="tip__icon" role="img" aria-label="Protein shaker icon" style="right:12px;border:none;background:#f2a66a;border-radius:4px;width:14px;height:24px;top:-8px"></span></div>
      <p class="tip__sub" style="font-size:8.2px">Especially Post-Workout or on Busy days</p>
    </div>
    <div class="tip" style="left:24px;top:79px">
      <div class="tip__bar center">Eat 3–4 meals per day<span class="tip__icon" role="img" aria-label="Fork and knife icon" style="left:12px;top:-4px;width:25px;height:25px"></span></div>
      <p class="tip__sub center">Every 3–4 Hours</p>
    </div>
    <div class="tip" style="left:219px;top:79px">
      <div class="tip__bar center">Post-Workout Meal =<span class="tip__icon" role="img" aria-label="Wheat grain icon" style="left:12px;top:-4px;width:25px;height:25px;border-color:#d89a2a"></span></div>
      <p class="tip__sub center">Protein + Carb, No added Fats</p>
    </div>
    <div class="tip" style="left:24px;top:115px">
      <div class="tip__bar">Protein for maintain muscle<span class="tip__icon" role="img" aria-label="Roast chicken icon" style="right:5px;top:-5px;width:25px;height:25px;border-color:#2a7fc2"></span></div>
      <p class="tip__sub wrap">Include protein in every meal to stabilize blood sugar and support muscle</p>
    </div>
    <div class="tip" style="left:219px;top:115px">
      <div class="tip__bar" style="font-size:8.2px;padding-right:30px">Limit “treat” meals to 1 per week<span class="tip__icon" role="img" aria-label="Plate icon" style="right:3px;top:-5px;width:25px;height:25px"></span></div>
      <p class="tip__sub">(keep it controlled)</p>
    </div>
  </section>

  <section class="panel habits">
    <h2 class="heading">OPTIONAL HABITS TO STACK</h2>
    <svg class="chev" style="left:361px;top:3px" width="30" height="18" viewBox="0 0 36 22" fill="none" stroke="#e07066" stroke-width="2"><path d="M2 2l9 9-9 9M12 2l9 9-9 9M22 2l9 9-9 9"/></svg>
    <div class="pill" style="left:16px;top:27px;width:172px">Weigh in once per week (same day/time)<span class="pill__icon" role="img" aria-label="Scale icon"></span></div>
    <div class="pill" style="left:213px;top:26px;width:192px;padding-left:31px">Keep a visible “YES/NO” food list on the fridge<span class="pill__icon" role="img" aria-label="Fridge note icon" style="background:#f3a23a"></span></div>
    <div class="pill" style="left:16px;top:48px;width:172px;padding-left:6px">Prep 2–3 proteins and veggies on Sunday<span class="pill__icon" role="img" aria-label="Calendar icon" style="left:auto;right:4px;background:#fff;border:1px solid #6a3a8a"></span></div>
    <div class="pill" style="left:213px;top:48px;width:192px;padding-left:5px;font-size:6.5px">Add a short 10-min walk after dinner to boost digestion<span class="pill__icon" role="img" aria-label="Walking figure icon" style="left:auto;right:3px;width:14px;height:14px;top:0;background:#f5d515;border-radius:50%"></span></div>
  </section>
</section>

</body>
</html>
```